Business Card for Veltrano, a french tech company

Tech company
New technologies
Serious design
Dark theme

User info :
Name: Mathis CORLAVE
Position: Co-Founder & CEO
Tel: (+33) 6 58 24 90 37
Email: mathis@veltrano.io
Website: www.veltrano.io
Address: 17 rue des Tanneurs 69002 LYON

Attached is the business logo file.

```html
<!DOCTYPE html>
<html lang="fr">
<head>
<meta charset="utf-8">
<title>Veltrano — Carte de visite</title>
<link rel="stylesheet" href="https://fonts.googleapis.com/css2?family=Open+Sans:wght@400;600;700&family=Montserrat:wght@700;800&display=swap">
<style>
  :root {
    --stage: #2f2f2f;
    --navy: #12103f;
    --navy-deep: #0f0d38;
    --teal: #18729a;
    --teal-mid: #1d5f8a;
    --magenta: #d9288f;
    --purple: #a33a9c;
    --violet: #8a4aa6;
    --ink: #1b1b1b;
    --paper: #ffffff;
  }
  * { box-sizing: border-box; margin: 0; padding: 0; }
  html, body {
    width: 1200px;
    height: 780px;
    overflow: hidden;
    background: var(--stage);
  }
  .sheet {
    position: relative;
    width: 1200px;
    height: 780px;
    display: flex;
    align-items: center;
    justify-content: center;
    gap: 40px;
  }
  .card {
    position: relative;
    width: 540px;
    height: 350px;
    overflow: hidden;
    box-shadow: 0 14px 30px rgba(0,0,0,0.45);
  }

  /* Back side */
  .card-back {
    background: linear-gradient(35deg, var(--navy-deep) 0%, var(--navy) 45%, #16406b 75%, var(--teal) 100%);
    display: flex;
    align-items: center;
    justify-content: center;
  }
  .back-name {
    font-family: "Montserrat", sans-serif;
    font-weight: 800;
    font-size: 56px;
    letter-spacing: 4px;
    color: var(--paper);
  }

  /* Front side */
  .card-front {
    background: var(--paper);
  }
  .name-tab {
    position: absolute;
    top: 32px;
    right: 0;
    width: 16px;
    height: 44px;
    background: linear-gradient(180deg, var(--violet), var(--magenta));
  }
  .identity {
    position: absolute;
    top: 30px;
    right: 30px;
    text-align: right;
    font-family: "Open Sans", sans-serif;
  }
  .person-name {
    font-weight: 700;
    font-size: 29px;
    line-height: 1.05;
    letter-spacing: 0.5px;
  }
  .first-name { color: var(--purple); }
  .last-name { color: var(--teal-mid); }
  .person-role {
    font-weight: 600;
    font-size: 14px;
    color: var(--ink);
    letter-spacing: 0.4px;
    margin-top: 2px;
  }
  .brand {
    position: absolute;
    left: 40px;
    top: 150px;
    display: flex;
    align-items: center;
    gap: 12px;
    font-family: "Open Sans", sans-serif;
    font-weight: 700;
    font-size: 40px;
    color: var(--navy);
  }
  .brand-mark {
    width: 18px;
    height: 18px;
    background: var(--magenta);
  }
  .contact {
    position: absolute;
    right: 30px;
    top: 138px;
    font-family: "Open Sans", sans-serif;
    font-size: 13.5px;
    color: var(--ink);
    text-align: right;
    line-height: 1.35;
  }
  .address { margin-bottom: 12px; padding-right: 24px; }
  .contact-line {
    display: flex;
    align-items: center;
    justify-content: flex-end;
    gap: 8px;
  }
  .contact-line svg { width: 16px; height: 16px; flex: none; }
  .footer-rule {
    position: absolute;
    left: 0; right: 0;
  }
  .rule-magenta { bottom: 48px; height: 3px; background: var(--magenta); }
  .rule-violet { bottom: 42px; height: 2px; background: var(--violet); }
  .footer-band {
    bottom: 0;
    height: 34px;
    background: linear-gradient(180deg, var(--teal) 0%, #155a86 45%, var(--navy) 100%);
  }
</style>
</head>
<body>
<main class="sheet">
  <section class="card card-back" aria-label="Verso de la carte">
    <span class="back-name">VELTRANO</span>
  </section>

  <section class="card card-front" aria-label="Recto de la carte">
    <div class="name-tab"></div>
    <header class="identity">
      <p class="person-name"><span class="first-name">Mathis</span> <span class="last-name">CORLAVE</span></p>
      <p class="person-role">Co-Founder &amp; CEO</p>
    </header>

    <div class="brand">
      <span class="brand-mark"></span>
      <span>Veltrano</span>
    </div>

    <address class="contact">
      <p class="address">17 rue des Tanneurs<br>69002 LYON</p>
      <p class="contact-line">(+33) 6 58 24 90 37
        <svg viewBox="0 0 16 16" aria-hidden="true"><path fill="#a33a9c" d="M4.2 1.5 6.3 4 5 5.6c.8 1.8 2.3 3.3 4.1 4.1l1.6-1.3 2.5 2.1-1.1 2.4C7 12.6 3.1 8.7 2 3.9Z"/></svg>
      </p>
      <p class="contact-line">www.veltrano.io
        <svg viewBox="0 0 16 16" aria-hidden="true"><circle cx="8" cy="8" r="6.5" fill="none" stroke="#a33a9c" stroke-width="1.5"/><path d="M1.5 8h13M8 1.5c-2.4 2.2-2.4 10.8 0 13M8 1.5c2.4 2.2 2.4 10.8 0 13" fill="none" stroke="#a33a9c" stroke-width="1.2"/></svg>
      </p>
      <p class="contact-line">mathis@veltrano.io
        <svg viewBox="0 0 16 16" aria-hidden="true"><rect x="1.5" y="3.5" width="13" height="9.5" rx="1" fill="none" stroke="#a33a9c" stroke-width="1.5"/><path d="m1.8 4 6.2 5 6.2-5" fill="none" stroke="#a33a9c" stroke-width="1.5"/></svg>
      </p>
    </address>

    <div class="footer-rule rule-magenta"></div>
    <div class="footer-rule rule-violet"></div>
    <div class="footer-rule footer-band"></div>
  </section>
</main>
</body>
</html>
```